Business card for denture clinic Gumlyssa

We need a new business card with our new logo. We are a denture clinic in New Zealand with our target market being 45+ years old. We would need a space on the back to write our patients next appointment on. We would space for only one appointment rather than a list. We will attach a photo showing an example of this. But of course, we would like to see your twist on this. We want it to be bold and easy to read and a good mixture of professional but modern. We have attached our logo to be used on the card.

Target Market(s)

People aged 45+ needing dentures

Industry/Entity Type

Dental

Contact Information for Business Card

We want our logo on the front and the space to write an appointment on the back. I've attached an example our our old business card showing this. We need to have the technicians details on the front.

Font styles to use
Sans Serif

Colors
0255a3
919191
fbfbfb

Requirements
Must have
• The following details:
• Ravi Pelling BDT, PGDipCDentTech Marlow
• Dental Prosthetist
• Phone numbers: 0800 47 2150
• 09 571 3294
• Email: ravi@gumlyssa.co.nz
• www.gumlyssa.co.nz
• Address: 418 Whiroa Road
• Kauriwhenua East
• Auckland 0610
Nice to have
• We would like our business cards to have more than just two colours as we want them to be more vibrant. We have uploaded an example of a business card we liked that showed this.

```html
<!DOCTYPE html>
<html lang="en">
<head>
<meta charset="utf-8">
<title>Gumlyssa — Business Card</title>
<link rel="stylesheet" href="https://fonts.googleapis.com/css2?family=Open+Sans:wght@400;600;700&display=swap">
<style>
  :root {
    --brand-blue: #0b6cb8;
    --brand-blue-deep: #0255a3;
    --band-grey: #919191;
    --paper: #fbfbfb;
    --white: #ffffff;
    --canvas: #e6e7e9;
    --faint-white: rgba(255,255,255,0.09);
    --faint-blue: rgba(11,108,184,0.05);
  }
  * { box-sizing: border-box; margin: 0; padding: 0; }
  html, body {
    width: 1200px; height: 1200px; overflow: hidden;
    background: var(--canvas);
    font-family: "Open Sans", Arial, sans-serif;
  }
  .canvas {
    width: 1200px; height: 1200px;
    display: flex; align-items: center; justify-content: center; gap: 44px;
  }
  .card {
    position: relative; overflow: hidden;
    box-shadow: 0 6px 22px rgba(0,0,0,0.16);
  }

  /* Front: logo + appointment slot */
  .card-front {
    width: 640px; height: 366px;
    background: var(--white);
  }
  .card-front .decor-circle {
    position: absolute; right: 40px; top: -40px;
    width: 300px; height: 300px; border-radius: 50%;
    background: var(--faint-blue);
  }
  .brand {
    position: absolute; left: 0; right: 0; top: 104px;
    display: flex; align-items: center; justify-content: center; gap: 18px;
  }
  .brand-square {
    width: 62px; height: 62px; background: var(--brand-blue-deep);
  }
  .brand-name {
    font-size: 60px; font-weight: 600; letter-spacing: 1px;
    color: var(--brand-blue-deep); line-height: 1;
  }
  .appointment-band { position: absolute; left: 0; bottom: 0; width: 640px; height: 110px; }
  .appointment-label {
    position: absolute; right: 34px; bottom: 56px;
    font-size: 17px; color: var(--brand-blue-deep);
  }
  .date-field {
    position: absolute; left: 30px; bottom: 22px;
    font-size: 18px; color: var(--white);
    display: flex; align-items: flex-end; gap: 8px;
  }
  .date-line {
    width: 200px; border-bottom: 2px dotted var(--white); margin-bottom: 5px;
  }

  /* Back: technician details */
  .card-back {
    width: 366px; height: 640px;
    background: var(--brand-blue);
    color: var(--white);
    text-align: center;
  }
  .card-back .decor-circle {
    position: absolute; right: -90px; top: 40px;
    width: 320px; height: 320px; border-radius: 50%;
    background: var(--faint-white);
  }
  .person { position: absolute; left: 0; right: 0; top: 62px; }
  .person-name { font-size: 46px; font-weight: 400; line-height: 1.1; }
  .person-credentials { font-size: 17px; margin-top: 8px; }
  .person-role { font-size: 26px; font-weight: 700; margin-top: 4px; }
  .contact { position: absolute; left: 0; right: 0; top: 278px; }
  .contact-item { display: flex; flex-direction: column; align-items: center; margin-bottom: 20px; }
  .contact-item:last-child { margin-bottom: 0; }
  .contact-item svg { margin-bottom: 8px; }
  .contact-text { font-size: 19px; line-height: 1.3; }
</style>
</head>
<body>
<main class="canvas">

  <section class="card card-front" aria-label="Card front">
    <div class="decor-circle"></div>
    <div class="brand">
      <div class="brand-square"></div>
      <div class="brand-name">Gumlyssa</div>
    </div>
    <svg class="appointment-band" viewBox="0 0 640 110" aria-hidden="true">
      <path d="M0 40 H300 C320 40 322 72 345 72 H640 V110 H0 Z" fill="var(--band-grey)"/>
    </svg>
    <p class="appointment-label">your next appointment</p>
    <p class="date-field">date <span class="date-line"></span></p>
  </section>

  <section class="card card-back" aria-label="Card back">
    <div class="decor-circle"></div>
    <div class="person">
      <h1 class="person-name">Ravi Pelling</h1>
      <p class="person-credentials">BDT, PGDipCDentTech Marlow</p>
      <p class="person-role">Dental Prosthetist</p>
    </div>
    <div class="contact">
      <div class="contact-item">
        <svg width="26" height="34" viewBox="0 0 26 34" aria-hidden="true">
          <path d="M13 1C6.4 1 1 6.2 1 12.8 1 21 13 33 13 33S25 21 25 12.8C25 6.2 19.6 1 13 1Z" fill="var(--white)"/>
          <circle cx="13" cy="12.5" r="5" fill="var(--brand-blue)"/>
        </svg>
        <p class="contact-text">418 Whiroa Road<br>Kauriwhenua East<br>Auckland 0610</p>
      </div>
      <div class="contact-item">
        <svg width="30" height="30" viewBox="0 0 24 24" aria-hidden="true">
          <path d="M6.6 10.8a15.2 15.2 0 0 0 6.6 6.6l2.2-2.2a1 1 0 0 1 1-.25 11.4 11.4 0 0 0 3.6.57 1 1 0 0 1 1 1V20a1 1 0 0 1-1 1A17 17 0 0 1 3 4a1 1 0 0 1 1-1h3.5a1 1 0 0 1 1 1c0 1.25.2 2.45.57 3.57a1 1 0 0 1-.25 1Z" fill="var(--white)"/>
        </svg>
        <p class="contact-text">0800 47 2150 / 09 571 3294</p>
      </div>
      <div class="contact-item">
        <svg width="40" height="26" viewBox="0 0 40 26" aria-hidden="true">
          <rect x="1" y="1" width="38" height="24" fill="var(--white)"/>
          <path d="M2 2 L20 15 L38 2" fill="none" stroke="var(--brand-blue)" stroke-width="2.5"/>
        </svg>
        <p class="contact-text">ravi@gumlyssa.co.nz<br>www.gumlyssa.co.nz</p>
      </div>
    </div>
  </section>

</main>
</body>
</html>
```